Brightgate Automotive Service Website Design

We are working with Brightgate Automotive Service. They are a local mechanic/garage and in need of a new website design.

Some sites to use for inspiration:

https://www.torvalle.example
https://www.quenby.example
https://parks-carcare.example
https://www.hollowmerefullautocare.example/

Thank you for taking the time to consider designing a website for us. We are web developers based in Stockton, CA, USA. Most of our projects go through the same process. Understanding this process may help you win a project with us. We custom-code all of our websites in-house. We don’t have any requirements as to what tools you use for your design, but we prefer Figma files. For any design that we label as four-stars, we send it to the client for review. The client picks the final design they want us to use. Once we complete this process, we will continue to show additional clients all the four-star sites and purchase them later. Your designs will have multiple chances to sell. For better chances of success, we ask that you follow these guidelines.

IMAGES:
If you use any images or icons in the design, we ask that you have a link to the asset so we can purchase the image/icon. Most of the designs we submit do not have the customer’s images on them unless they have some great images. Be creative; show us the feeling you are trying to portray with your image choices. Use any royalty-free site you choose. We subscribe to Adobe and mainly use their images, but we can purchase images outside of Adobe.

PLEASE NOTE: we will not submit designs to clients with watermarks on the images.

FONTS:
We ask that you identify the fonts used in the design. This can be done in a message if you want. We typically use Google Fonts and Adobe Fonts.

CONTENT:
We're always open to different content and ideas. We often submit designs with stock images so the client can see our vision. We typically take pictures after the website launch to use their images with our vision. Lorem Ipsum is fine for paragraphs, but we ask that you write the headers in correct English. We want to be able to show the vision and identify the sections of the website.

INSPIRATION:
We typically add a couple of links in the brief of websites we like to help you get started in your design.

REVISIONS:
We do not often ask for revisions of the designs unless we see something in the design that may not appeal to the client. If there are slight changes that we want to make, we do that in the development process.

FEEDBACK:
We rarely give feedback on designs during the design process. We are working on many website projects and do not have the time to provide feedback. We usually respond if your request is well thought out and asks specific questions, but a note asking “feedback, please” usually goes unanswered.

```html
<!DOCTYPE html>
<html lang="en">
<head>
<meta charset="utf-8">
<title>Brightgate Automotive Service</title>
<link href="https://fonts.googleapis.com/css2?family=Poppins:wght@400;500;600;700;800&display=swap" rel="stylesheet">
<style>
:root{
  --red:#c4161c;
  --ink:#14161c;
  --navy:#0d1522;
  --text:#5b5f66;
  --line:#e3e4e8;
  --soft:#eef0f4;
  --white:#fff;
}
*{box-sizing:border-box;margin:0;padding:0}
html,body{width:1200px;height:3984px;overflow:hidden}
body{font-family:"Poppins",sans-serif;color:var(--ink);background:var(--white);position:relative}
a{color:inherit;text-decoration:none}
ul{list-style:none}
.btn{display:inline-block;background:var(--red);color:#fff;font-weight:600;font-size:13px;letter-spacing:.5px;text-transform:uppercase;padding:12px 22px;white-space:nowrap}
.photo{display:block}

/* top bar */
.topbar{height:36px;background:var(--navy);color:#fff;font-size:12px;display:flex;align-items:center;justify-content:space-between;padding:0 56px}
.topbar .social{display:flex;gap:10px;align-items:center}
.dot{width:12px;height:12px;border-radius:50%;background:#fff;display:inline-block}
.topbar .meta{display:flex;gap:24px}

/* header */
.header{height:96px;display:flex;align-items:center;padding:0 64px}
.brand{font-size:38px;font-weight:800;color:var(--ink);letter-spacing:-1px;display:flex;align-items:center;gap:10px;white-space:nowrap}
.brand .sq{width:14px;height:14px;background:var(--red)}
.search{margin-left:110px;width:420px;height:40px;border:1px solid var(--line);border-radius:20px;display:flex;align-items:center;justify-content:space-between;padding:0 18px;color:#999;font-size:13px}
.support{margin-left:auto;display:flex;align-items:center;gap:12px;font-size:12px;line-height:1.5}
.support .ic{width:36px;height:36px;border-radius:50%;background:var(--red);flex-shrink:0}
.support b{display:block;font-weight:600}
.nav{height:48px;display:flex;align-items:center;padding:0 64px;border-top:1px solid var(--line);border-bottom:3px solid var(--red)}
.nav a{font-size:13px;font-weight:500;margin-right:58px;text-transform:uppercase}
.nav a.on{color:var(--red)}
.nav .btn{margin:0 0 0 auto;padding:10px 30px}

/* hero */
.hero{position:relative;height:640px;background:linear-gradient(100deg,#0b0c10 0%,#1c1d22 45%,#3a1214 100%);overflow:hidden}
.hero .wheels{position:absolute;right:70px;top:80px;width:460px;height:460px;border-radius:50%;background:radial-gradient(circle,#8d9096 0%,#3b3d42 55%,#111 72%,transparent 73%)}
.hero .copy{position:absolute;left:64px;top:150px;color:#fff}
.hero small{font-size:22px;letter-spacing:1px;text-transform:uppercase}
.hero h1{font-size:52px;font-weight:700;line-height:1.15;margin:10px 0 18px;width:680px}
.hero p{font-size:17px;width:540px;line-height:1.5;color:#ddd}
.hero .btn{background:#fff;color:var(--ink);margin-top:26px}

/* services + about */
.about{display:flex;padding:0 64px;margin-top:70px;gap:30px;height:300px}
.sidebar{width:240px;flex-shrink:0;border:1px solid var(--line);align-self:flex-start}
.sidebar h4{background:var(--soft);padding:12px 18px;font-size:16px;font-weight:600}
.sidebar li{padding:11px 18px;border-top:1px solid var(--line);font-size:13px;display:flex;gap:12px;align-items:center;white-space:nowrap}
.sidebar li i{width:16px;height:16px;border:2px solid var(--red);border-radius:50%;flex-shrink:0}
.about-text h2{font-size:30px;font-weight:600;margin-bottom:14px}
.about-text p{font-size:13px;color:var(--text);line-height:1.6;margin-bottom:12px}

/* promo row */
.promo{display:flex;padding:0 64px;margin-top:50px;gap:30px;height:420px}
.summer{width:240px;flex-shrink:0;height:420px;background:var(--soft);padding:30px 18px;position:relative;overflow:hidden}
.summer h3{font-size:30px;font-weight:500;line-height:1.15;color:#333}
.summer p{font-size:11px;color:var(--text);margin:10px 0}
.summer .btn{font-size:10px;padding:8px 12px}
.summer .tires{position:absolute;left:0;bottom:0;width:200px;height:170px;background:linear-gradient(#2b2c30,#0d0d10);border-radius:0 80px 0 0}
.media{flex:1}
.video{height:250px;position:relative;background:linear-gradient(90deg,#1a0b0c,#4b1517 60%,#1c1c20)}
.video .play{position:absolute;left:50%;top:50%;width:56px;height:56px;margin:-28px 0 0 -28px;border-radius:50%;background:var(--red)}
.video .play:after{content:"";position:absolute;left:22px;top:17px;border-left:16px solid #fff;border-top:11px solid transparent;border-bottom:11px solid transparent}
.parts{display:flex;justify-content:space-between;margin-top:30px}
.parts .photo{width:110px;height:130px;background:radial-gradient(circle,#b9bcc2,#eceef1 70%)}

/* testimonials */
.clients{position:absolute;left:0;top:1740px;width:1200px;height:520px;background:var(--soft);text-align:center}
.clients h2{font-size:34px;font-weight:500;margin-top:58px}
.cards{display:flex;justify-content:center;gap:40px;margin-top:46px}
.quote{width:420px;height:220px;background:#fff;text-align:left;padding:36px 40px}
.quote .who{display:flex;align-items:center;gap:14px}
.quote .avatar{width:56px;height:56px;background:#c9ccd2;flex-shrink:0}
.quote b{font-size:15px;font-weight:600;display:block}
.quote .mark{margin-left:auto;color:var(--red);font-size:60px;font-weight:700;line-height:1}
.quote p{font-size:15px;color:var(--text);margin-top:26px;line-height:1.45}
.clients .btn{margin-top:40px;font-size:11px}

/* feature band */
.band{position:absolute;left:0;top:2260px;width:1200px;height:560px;overflow:hidden}
.band svg{position:absolute;left:0;top:0}
.band .scene{position:absolute;left:240px;top:60px;width:680px;height:500px;background:linear-gradient(90deg,rgba(150,154,160,.55),rgba(44,79,140,.55))}

/* blog */
.blog{position:absolute;left:0;top:2840px;width:1200px;text-align:center}
.blog h2{font-size:34px;font-weight:500;line-height:50px}
.posts{display:flex;justify-content:center;gap:36px;margin-top:130px}
.post{width:520px;height:400px;background:var(--soft);display:flex;text-align:left}
.post .body{width:260px;padding:40px 24px}
.post .tag{font-size:11px;font-weight:600;text-transform:uppercase;color:var(--red)}
.post .date{font-size:11px;color:var(--text)}
.post h3{font-size:20px;font-weight:600;line-height:1.3;margin:26px 0 14px}
.post p{font-size:12px;color:var(--text);line-height:1.5}
.post .more{display:block;margin-top:22px;font-size:11px;font-weight:600;color:var(--red)}
.post .photo{width:260px;height:100%;background:linear-gradient(#c9cdd4,#7b8089)}
.blog .btn{margin-top:60px;font-size:11px}

/* footer */
.footer{position:absolute;left:0;top:3600px;width:1200px;height:384px;background:var(--navy);color:#fff}
.footer .cols{display:flex;padding:70px 64px 0}
.footer .col1{width:500px}
.footer .col1 p{font-size:13px;color:#bcc1ca;width:240px;margin-top:14px;line-height:1.5}
.footer .brand{color:#fff}
.footer .socials{display:flex;gap:18px;margin-top:20px}
.footer h4{font-size:20px;font-weight:500;margin-bottom:18px}
.footer .col2{width:320px}
.footer .col2 li{font-size:13px;margin-bottom:12px}
.footer .col3 li{font-size:13px;margin-bottom:14px;display:flex;gap:12px;align-items:center}
.footer .col3 i{width:22px;height:22px;border-radius:50%;background:var(--red)}
.footer .copy{position:absolute;bottom:0;left:0;width:100%;height:46px;border-top:1px solid #26303f;text-align:center;line-height:46px;font-size:12px}
</style>
</head>
<body>

<div class="topbar">
  <div class="social">Follow With Us <span class="dot"></span><span class="dot"></span><span class="dot"></span><span class="dot"></span></div>
  <div class="meta"><span>Store Locator</span><span>We Are Different</span></div>
</div>

<header class="header">
  <a class="brand"><span class="sq"></span>BRIGHTGATE</a>
  <div class="search">Search <span>&#9906;</span></div>
  <div class="support"><span class="ic"></span><div><b>Support 209 555 0143</b>Email: hello@brightgate.example</div></div>
</header>

<nav class="nav">
  <a class="on">Home</a><a>About Us</a><a>Location</a><a>Services</a><a>Rewards</a><a>Contact Us</a>
  <a class="btn">Book Now</a>
</nav>

<section class="hero">
  <div class="wheels photo" role="img" aria-label="Chrome alloy wheels with tyres on a dark background"></div>
  <div class="copy">
    <small>Welcome to Brightgate</small>
    <h1>Providing Automotive Repair Services</h1>
    <p>Trusted repairs done right the first time, by certified mechanics who treat your car like their own.</p>
    <a class="btn">Learn More &rsaquo;</a>
  </div>
</section>

<section class="about">
  <div class="sidebar">
    <h4>Our Services</h4>
    <ul>
      <li><i></i>Oil Change</li>
      <li><i></i>Exhaust &amp; Mufflers</li>
      <li><i></i>Brakes</li>
      <li><i></i>Tires &amp; Wheels</li>
      <li><i></i>A/C</li>
      <li><i></i>Steering &amp; Suspension</li>
    </ul>
  </div>
  <div class="about-text">
    <h2>Welcome to Brightgate Car Care Center</h2>
    <p>Located in Stockton, CA, Brightgate Car Care Center is a certified shop whose technicians are experienced in all types of automotive repair, including brake replacement, cooling system conditioning and heating, electrical issues, power windows, catalytic converters, batteries, shocks and struts, water pump replacement, timing belts, mufflers and custom exhaust services.</p>
    <p>The check engine light on in your dashboard? We can fix your car. Our shop works on all makes and models of cars and trucks, and installs quality aftermarket parts. We are a Corvane AutoCare Center, and repairs carry a warranty of 36 months and 36,000 miles.</p>
    <p>The check engine light on in your dashboard? We can fix your car. Our shop works on all makes and models of cars and trucks, and installs quality aftermarket parts.</p>
    <a class="btn">Learn More</a>
  </div>
</section>

<section class="promo">
  <div class="summer">
    <h3>Summer Essentials</h3>
    <p>Keep your tyres in top shape before the long summer drives begin.</p>
    <a class="btn">Tip The Tire Decision</a>
    <div class="tires photo" role="img" aria-label="Stack of new car tyres"></div>
  </div>
  <div class="media">
    <div class="video photo" role="img" aria-label="Video still of a sports car in a dark garage"><span class="play"></span></div>
    <div class="parts">
      <div class="photo" role="img" aria-label="Car engine"></div>
      <div class="photo" role="img" aria-label="Brake disc and caliper"></div>
      <div class="photo" role="img" aria-label="Shock absorber"></div>
      <div class="photo" role="img" aria-label="Car tyre"></div>
      <div class="photo" role="img" aria-label="Car battery"></div>
      <div class="photo" role="img" aria-label="Headlight unit"></div>
    </div>
  </div>
</section>

<section class="clients">
  <h2>Happy Clients</h2>
  <div class="cards">
    <div class="quote">
      <div class="who"><span class="avatar photo" role="img" aria-label="Customer portrait"></span><div><b>Mara Ellison</b><b>Fernwick Holdings Ltd.</b></div><span class="mark">&ldquo;</span></div>
      <p>It was pleasure to work with the team. It's helped us in our contributed his technical expertise.</p>
    </div>
    <div class="quote">
      <div class="who"><span class="avatar photo" role="img" aria-label="Customer portrait"></span><div><b>Mara Ellison</b><b>Fernwick Holdings Ltd.</b></div><span class="mark">&ldquo;</span></div>
      <p>It was pleasure to work with the team. It's helped us in our contributed his technical expertise.</p>
    </div>
  </div>
  <a class="btn">View All Testimonial</a>
</section>

<section class="band">
  <svg width="1200" height="560" viewBox="0 0 1200 560" aria-hidden="true">
    <rect width="1200" height="560" fill="#b5151a"/>
    <path d="M0 200 C300 460 900 460 1200 200 L1200 560 L0 560 Z" fill="#fff"/>
  </svg>
  <div class="scene photo" role="img" aria-label="Mechanic in blue overalls standing beside a silver SUV with its bonnet open"></div>
</section>

<section class="blog">
  <h2>Latest Blog</h2>
  <div class="posts">
    <article class="post">
      <div class="body">
        <div class="tag">Ashford</div><div class="date">Nov 25, 2023</div>
        <h3>How to Choose the Best In-Home Pet Care Service</h3>
        <p>Consectetuer fringilla semper sodales potenti ullamcorper nam porta feugiat. Ante urna congue feugiat effictur vel duis.</p>
        <a class="more">Learn More &rsaquo;</a>
      </div>
      <div class="photo" role="img" aria-label="Technician checking a car with a tablet"></div>
    </article>
    <article class="post">
      <div class="body">
        <div class="tag">Ashford</div><div class="date">Nov 25, 2023</div>
        <h3>How to Choose the Best In-Home Pet Care Service</h3>
        <p>Consectetuer fringilla semper sodales potenti ullamcorper nam porta feugiat. Ante urna congue feugiat effictur vel duis.</p>
        <a class="more">Learn More &rsaquo;</a>
      </div>
      <div class="photo" role="img" aria-label="Mechanic holding a wrench in a workshop"></div>
    </article>
  </div>
  <a class="btn">View All Blog</a>
</section>

<footer class="footer">
  <div class="cols">
    <div class="col1">
      <a class="brand"><span class="sq"></span>BRIGHTGATE</a>
      <p>It is a long established fact that a reader will be distracted by the readable content of a page when looking at its layout.</p>
      <div class="socials"><span class="dot"></span><span class="dot"></span><span class="dot"></span></div>
    </div>
    <div class="col2">
      <h4>Quick Links</h4>
      <ul><li>Home</li><li>About Us</li><li>Services</li><li>Location</li><li>Contact Us</li></ul>
    </div>
    <div class="col3">
      <h4>Contact Us</h4>
      <ul>
        <li><i></i>+1 209 555 0143</li>
        <li><i></i>service@brightgate.example</li>
        <li><i></i>122, Harbor Lane, Stockton</li>
      </ul>
    </div>
  </div>
  <div class="copy">Copyright &copy; 2023 Brightgate. All rights reserved.</div>
</footer>

</body>
</html>
```